Webdesign für visa-korvenet.org
Kreativer Initialvorschlag, schnelle Umsetzung, flexible Anpassung des Designvorschlags und nette Kommunikation, gerne wieder!
Zielgruppe
Wir vermitteln weltweit Reisegenehmigungen für Geschäfts- und Privatkunden. Auf VISA-Korvenet.org möchten wir auf deutsch, englisch & chinesisch Reisenden bei der Beiholung von Kurzzeit, Work & Travel & diversen Visaarten helfen.
Aufgabenstellung
Der Webseitezweck ist es, dass Besucher bestellen. Dafür muss die Seite attraktiv, einfach bedienbar und das CTA Element "zum Formular" präsent und mehrfach auftauchen.

```html
<!DOCTYPE html>
<html lang="de">
<head>
<meta charset="utf-8">
<title>Visa Korvenet – Evisitor Visum Australien</title>
<link href="https://fonts.googleapis.com/css2?family=Lato:wght@300;400;700;900&family=Arimo:wght@400;700&display=swap" rel="stylesheet">
<style>
:root{
  --blue:#0b4f9e;
  --blue-dark:#083d7c;
  --red:#c8102e;
  --red-dark:#a50c24;
  --grey-bg:#f2f2f2;
  --card-bg:#efefef;
  --row-alt:#dce8f5;
  --row:#eef3f9;
  --text:#444;
  --text-dark:#222;
  --white:#fff;
}
*{box-sizing:border-box;margin:0;padding:0}
html,body{width:1200px;height:3426px;overflow:hidden}
body{font-family:"Lato",sans-serif;color:var(--text);background:var(--white);position:relative}
.ui{font-family:"Arimo",sans-serif}
a{color:var(--blue);text-decoration:none}

/* Header */
.site-header{position:absolute;top:0;left:0;width:1200px;height:132px;background:linear-gradient(#fff,#f4f6f9)}
.brand{position:absolute;left:37px;top:48px;display:flex;align-items:center;gap:12px}
.brand-mark{width:26px;height:26px;border-radius:50%;background:var(--blue)}
.brand-name{font-size:30px;font-weight:700;color:var(--blue)}
.brand-sub{position:absolute;left:127px;top:88px;font-size:12px;font-style:italic;color:#333}
.header-cta{position:absolute;left:498px;top:60px;width:307px;height:38px;background:var(--red);border-radius:5px;color:#fff;font-weight:700;font-size:15px;display:flex;align-items:center;justify-content:center;box-shadow:0 2px 3px rgba(0,0,0,.25)}
.help{position:absolute;right:37px;top:22px;text-align:right;font-size:14px;line-height:17px;color:#333}
.help b{color:#222}
.help .blue{color:var(--blue)}
.help .red{color:var(--red);font-weight:700}
.help .redn{color:var(--red)}
.cards{display:flex;gap:8px;justify-content:flex-end;margin-top:10px}
.card-chip{width:45px;height:28px;border-radius:3px;border:1px solid #ccc;background:#e4e8ee}
.card-chip.b{background:#d7e1ee}.card-chip.c{background:#f2f2f2}

/* Nav */
.main-nav{position:absolute;top:132px;left:0;width:1200px;height:44px;background:var(--blue);border-bottom:3px solid var(--red);display:flex;padding-left:37px}
.main-nav a{color:#fff;font-weight:700;font-size:15px;line-height:41px;padding:0 13px;margin-right:16px}
.main-nav a.active{background:var(--red)}

/* Hero */
.hero{position:absolute;top:176px;left:0;width:1200px;height:438px}
.hero-img{position:absolute;inset:0;background:linear-gradient(180deg,#1b3a6b 0%,#3a5f91 30%,#c97b2c 58%,#6a3a18 75%,#1f3456 100%)}
.hero-title{position:absolute;left:37px;top:114px;font-size:57px;font-weight:300;color:#fff;letter-spacing:1px;line-height:1}
.hero-sub{position:absolute;left:37px;top:176px;font-size:25px;font-weight:700;color:#fff;text-shadow:0 1px 3px rgba(0,0,0,.6)}
.hero-box{position:absolute;left:37px;top:220px;width:484px;height:70px;background:rgba(20,20,20,.75);border-radius:6px}
.hero-btn{position:absolute;left:11px;top:14px;width:184px;height:38px;background:var(--red);border-radius:4px;color:#fff;font-weight:700;font-size:15px;display:flex;align-items:center;justify-content:center}
.hero-call{position:absolute;left:265px;top:20px;color:#fff;font-size:13px;line-height:15px}

/* Intro */
.intro{position:absolute;top:614px;left:0;width:1200px;height:222px;background:var(--grey-bg);text-align:center}
.intro h1{font-size:33px;font-weight:400;color:var(--text-dark);margin-top:24px}
.intro .sub{font-size:18px;color:#666;font-weight:300}
.intro p{font-size:15px;line-height:20px;color:#555;width:670px;margin:22px auto 0}
.more-btn{display:inline-block;margin-top:16px;width:146px;height:35px;line-height:33px;border:1px solid #999;font-size:14px;color:#555;background:#fafafa}

/* Feature cards */
.feature{position:absolute;top:873px;width:347px;height:509px;background:var(--card-bg)}
.feature .img{height:184px}
.feature h2{font-size:21px;font-weight:400;color:#333;margin:16px 13px 0}
.feature h2 span{color:var(--blue)}
.feature .tag{font-size:14px;color:var(--red);margin:2px 13px 0}
.feature p{font-size:13.5px;line-height:19.5px;color:#555;margin:14px 13px 0}
.feature p+p{margin-top:8px}
.feature ul{list-style:none;margin:24px 13px 0 15px;font-size:12px;line-height:20px;color:#555}
.feature li::before{content:"•";color:#888;margin-right:8px}
.feature .bar{position:absolute;left:0;bottom:0;width:347px;height:50px;background:var(--blue);color:#fff;font-weight:700;font-size:14.5px;line-height:50px;padding-left:44px}
.feature .bar.small{font-size:13px}
.feature .bar svg{position:absolute;left:0;top:0}

/* Advantages */
.advantages{position:absolute;top:1490px;left:0;width:1200px;height:612px;background:linear-gradient(90deg,#f1f3f6 0%,#f6f7f9 55%,#e3e8ee 100%)}
.adv-photo{position:absolute;right:0;top:0;width:330px;height:612px;background:linear-gradient(180deg,#e9ddd5 0%,#c98f6e 35%,#b5443f 65%,#e9eef3 100%)}
.adv-screen{position:absolute;left:885px;top:376px;width:260px;height:230px;background:#e8edf2;display:flex;align-items:center;justify-content:center;gap:8px;font-weight:700;font-size:16px;color:var(--blue)}
.adv-screen i{width:14px;height:14px;border-radius:50%;background:var(--blue)}
.advantages h2{position:absolute;left:35px;top:52px;font-size:26px;font-weight:400;color:#333;line-height:33px}
.advantages h2 a{color:var(--blue)}
.advantages h2 .red{color:var(--red)}
.compare{position:absolute;left:37px;top:135px;width:845px;border-collapse:collapse;font-size:12px;font-weight:700}
.compare th{background:var(--blue);color:#fff;height:41px;text-align:left;font-size:13px;font-weight:400}
.compare th:first-child{padding-left:17px}
.compare th.c{text-align:center}
.compare td{height:26.5px;padding-left:17px;color:#333}
.compare td.c{text-align:center;padding:0}
.compare tr:nth-child(odd) td{background:var(--row)}
.compare tr:nth-child(even) td{background:var(--row-alt)}

/* FAQ */
.faq{position:absolute;top:2159px;left:37px;width:648px}
.faq-q{height:42px;background:#e6edf5;display:flex;align-items:center;padding-left:14px;color:var(--blue);font-size:14px;margin-bottom:3px;font-family:"Arimo",sans-serif}
.faq-q .ic{font-size:26px;font-weight:700;margin-right:12px;width:18px;line-height:1}
.faq-q.open{background:var(--blue);color:#fff}
.faq-a{padding:14px 16px 10px;font-size:13.5px;line-height:20px;color:#555}
.faq-a p+p{margin-top:20px}
.faq-a+.faq-q{margin-top:4px}
.faq-side{position:absolute;top:2159px;left:705px;width:458px;height:512px;background:#fafafa;padding:24px 24px;font-size:13.5px;line-height:20px;color:#555;text-align:justify}
.faq-side p+p{margin-top:20px}

/* Callback */
.callback{position:absolute;top:2743px;left:0;width:1200px;height:221px;background:var(--red-dark);overflow:hidden}
.callback .blue-side{position:absolute;inset:0;background:var(--blue);clip-path:polygon(660px 0,1200px 0,1200px 221px,555px 221px)}
.callback h2{position:absolute;left:35px;top:58px;color:#fff;font-size:27px;font-weight:400}
.callback .lead{position:absolute;left:37px;top:98px;width:510px;color:#fff;font-size:13px;line-height:20px}
.callback .label{position:absolute;left:666px;top:56px;color:#fff;font-size:13px}
.field{position:absolute;height:37px;background:#fff;border:1px solid #cfd8e4;font-size:12.5px;color:var(--blue);padding-left:11px;line-height:35px}
.send{position:absolute;left:886px;top:131px;width:104px;height:37px;background:var(--red);color:#fff;font-weight:700;font-size:12.5px;line-height:37px;text-align:center}

/* Map */
.map{position:absolute;top:2964px;left:0;width:1200px;height:324px;background:linear-gradient(90deg,#e4e4e4,#ececec 50%,#dfe6d8)}

/* Footer */
.site-footer{position:absolute;top:3288px;left:0;width:1200px;height:138px;background:var(--blue);color:#fff}
.foot-col{position:absolute;top:22px;font-size:12px;line-height:18px}
.foot-col h3{font-size:17px;font-weight:700;margin-bottom:8px}
.foot-col a{color:#fff;display:block}
.foot-help{position:absolute;right:37px;top:22px;text-align:right;font-size:14px;line-height:17px}
</style>
</head>
<body>

<header class="site-header">
  <div class="brand"><span class="brand-mark"></span><span class="brand-name">Visa Korvenet</span></div>
  <div class="brand-sub">deutsches Formular - Visum Australien</div>
  <a class="header-cta ui" href="#">JETZT EVISITOR VISUM REGISTRIEREN</a>
  <div class="help ui">
    <b>Sie brauchen Hilfe?</b><br>
    Service Hotline von <span class="blue">Mo-Fr 10-16 Uhr</span><br>
    <span class="red">Kostenfrei:</span> <span class="redn">0800 555210480</span>
    <div class="cards"><span class="card-chip b"></span><span class="card-chip"></span><span class="card-chip c"></span></div>
  </div>
</header>

<nav class="main-nav ui">
  <a class="active" href="#">STARTSEITE</a>
  <a href="#">TOURISTEN VISUM</a>
  <a href="#">BUSINESS VISUM</a>
  <a href="#">WAS IST ETA</a>
  <a href="#">AGB</a>
  <a href="#">KONTAKT</a>
</nav>

<section class="hero">
  <div class="hero-img" role="img" aria-label="Hafenbrücke und Skyline von Sydney im Abendlicht"></div>
  <div class="hero-title">AUSTRALIA</div>
  <div class="hero-sub">Tourist und Business Visa</div>
  <div class="hero-box ui">
    <a class="hero-btn" href="#">JETZT REGISTRIEREN</a>
    <div class="hero-call">Oder rufen Sie <b>0800 555210480</b><br>an Telefonisch buchen</div>
  </div>
</section>

<section class="intro">
  <h1>Evisitor Visum Australien</h1>
  <div class="sub">(Bis 2008 ETA Electronic Travel Authority Australia)</div>
  <p>Touristen und Geschäftsleute benötigen zur Einreise nach Australien vor Reisebeginn ein gültiges Visum, kurz „eVisitor“.Bis 2008 hieß dieses Visum noch (Electronic Travel Authority).</p>
  <a class="more-btn" href="#">WEITERLESEN</a>
</section>

<article class="feature" style="left:37px">
  <div class="img" role="img" aria-label="Opernhaus und Hafen von Sydney" style="background:linear-gradient(180deg,#8fb8e0 0%,#cfdde9 50%,#2f6b9c 100%)"></div>
  <h2>eVisitor <span>Tourist ETA</span></h2>
  <div class="tag">mit 12 Monaten Gültigkeit</div>
  <p>Mit dem Visitor Visum können Touristen bis zu drei Monaten am Stück nach Australien reisen um dort Urlaub zu machen, Verwandte oder Bekannte zu besuchen. Eine arbeitsbezogene Nutzung dieses Visums ist ausdrücklich <b>nicht</b> gestattet!</p>
  <p><b>Wichtig:</b> Es muss bereits vor Antritt der Reise ein gültiges Visum vorliegen. Drucken Sie Ihre eVisitor Nummer aus und legen Sie diese Ihren Reisedokumenten bei.</p>
  <a class="bar ui" href="#"><svg width="28" height="50"><polygon points="0,0 28,25 0,50" fill="#fff"/></svg>JETZT EVISITOR VISUM REGISTRIEREN</a>
</article>

<article class="feature" style="left:425px">
  <div class="img" role="img" aria-label="Geschäftsreisender mit Laptop am Flughafen" style="background:linear-gradient(180deg,#6c6f78 0%,#a9acb2 45%,#2f5fa8 75%,#3b3d44 100%)"></div>
  <h2>eVisitor <span>Business ETA</span></h2>
  <div class="tag">mit 12 Monaten Gültigkeit</div>
  <p>Geschäftsreisende benötigen ein Business eVisitor Visum. Dieses ebenso elektronisch erstellte Visum hat einen Gültigkeit von 12 Monaten und kann für einen durchgängigen Geschäftsaufenthalt für bis zu drei Monaten genutzt werden. Wir empfehlen auch bei Messebesuchen ein Business Visum zu beantragen um eine problemlose Einreise zu gewährleisten.</p>
  <p><b>Wichtig:</b> Es muss bereits vor Antritt der Reise ein</p>
  <a class="bar ui" href="#"><svg width="28" height="50"><polygon points="0,0 28,25 0,50" fill="#fff"/></svg>JETZT EVISITOR VISUM REGISTRIEREN</a>
</article>

<article class="feature" style="left:814px">
  <div class="img" role="img" aria-label="Visum-Seite in einem Reisepass" style="background:linear-gradient(135deg,#b8c8c4 0%,#8fa4b8 45%,#3b4f73 100%)"></div>
  <h2>Welche <span>Dokumente</span> erhalte ich</h2>
  <div class="tag">mit meinem Evisitor Visum?</div>
  <p>Sobald Ihre Evisitor Genehmigung erteilt worden ist erhalten Sie eine Bestätigung per Email. Dieses Dokument müssen Sie aufheben und mit Ihren Reisedokumenten zur Reise mitnehmen. Die Evisitor Dokumente umfassen</p>
  <ul>
    <li>Ihre eVisitor Genehmigungsnummer</li>
    <li>Das Datum ab dem Ihre eVisitor Nummer gültig ist</li>
    <li>Die allgemeinen eVisitor Konditionen und Bedingungen</li>
  </ul>
  <a class="bar small ui" href="#"><svg width="28" height="50"><polygon points="0,0 28,25 0,50" fill="#fff"/></svg>DOCUMENT REQUIREMENT LESEN SIE MEHR</a>
</article>

<section class="advantages">
  <div class="adv-photo" role="img" aria-label="Lächelnde Frau mit Laptop"></div>
  <div class="adv-screen"><i></i>Visa Korvenet</div>
  <h2>Ihre Vorteile mit <a href="#">www.visa-korvenet.org</a><br><span class="red">in der Übersicht</span></h2>
  <table class="compare ui">
    <colgroup><col style="width:560px"><col style="width:150px"><col style="width:135px"></colgroup>
    <tr><th>UNSER SERVICE</th><th class="c">VISA-KORVENET.ORG</th><th class="c">EINREISE-PORTAL</th></tr>
    <tr><td>Anmeldeformular auf deutsch</td><td class="c">✓</td><td class="c"></td></tr>
    <tr><td>Hilfe bei der Formulareingabe</td><td class="c">✓</td><td class="c"></td></tr>
    <tr><td>Email Support</td><td class="c">✓</td><td class="c"></td></tr>
    <tr><td>Auf Wunsch auch Sendung der ETA Nummer per Post</td><td class="c">✓</td><td class="c"></td></tr>
    <tr><td>FAQ Section</td><td class="c">✓</td><td class="c">✓</td></tr>
    <tr><td>Kontrolle Ihrer gemachten Eingaben</td><td class="c">✓</td><td class="c">✓</td></tr>
    <tr><td>Rückmeldung und Überprüfung ob Ihre Eingaben abgeschickt wurden</td><td class="c">✓</td><td class="c">✓</td></tr>
    <tr><td>Manuelle Kontrolle bei Falscheingaben und Rückmeldung durch Supportmitarbeiter</td><td class="c">✓</td><td class="c"></td></tr>
    <tr><td>Statusnachricht Ihres ETA-Antrages</td><td class="c">✓</td><td class="c"></td></tr>
    <tr><td>ETA-Nummer Versand bequem per PDF</td><td class="c">✓</td><td class="c"></td></tr>
    <tr><td>Aufbewahrung Ihrer ETA Nummer für ein Jahr</td><td class="c">✓</td><td class="c">✓</td></tr>
    <tr><td>Kostenlose Neuanforderung Ihrer ETA Nummer innerhalb eines Jahres bei Verlust</td><td class="c">✓</td><td class="c">✓</td></tr>
    <tr><td>Garantierte Rückerstattung der Gebührenkosten, falls Ihre ETA Genehmigung zurückgewiesen wird</td><td class="c">✓</td><td class="c"></td></tr>
  </table>
</section>

<section class="faq">
  <div class="faq-q"><span class="ic">+</span>Wann erhalte ich meine Evisitor ETA VISA Genehmigung?</div>
  <div class="faq-q"><span class="ic">+</span>Was darf man als eVisitor (Inhaber eines ETA Visum) in Australien machen?</div>
  <div class="faq-q open"><span class="ic">–</span>3 Tipps für eine erfolgreiche Australien Reise</div>
  <div class="faq-a">
    <p>Gültige Reisedokumente für die gesamte Dauer des Aufenthaltes. Reisepass und vorläufiger Reisepass werden anerkannt. Kinder benötigen einen eigenen Reisepass. Personalausweis und vorläufiger Personalausweis sind nicht zugelassen Sollten asiatische Staaten im Zuge der Reise besucht werden wollen, informieren Sie sich bitte über die speziellen Vorschriften, da manche Staaten eine Gültigkeit bis zu sechs Monaten ausländischer Reisepässe voraussetzen.</p>
    <p>Australien hat sehr strikte Einreise und Quarantänevorschriften. An etlichen Flughäfen ist mit Körperscannern bei der Einreise zu rechnen. Ebenso müssen eingeführte Nahrungsmittel, Tier- und Pflanzenprodukte auf der Einreisekarte angegeben werden. Striktes Befolgen der Anweisungen wird von uns empfohlen um unnötige Wartezeiten und Ärger zu vermeiden.</p>
    <p>Halten Sie sich an die Gesetze des Landes. Wie bereits erwähnt ist Australien ein liberales Land, solange die Gesetze befolgt werden. Illegale Aktivitäten wie Verstöße gegen die Visa Bestimmungen, die Ausfuhr von kulturellen Schätzen oder die Einnahme von illegalen Substanzen können zur Ausweisung bis hin zu Freiheitstrafe in Australien führen.</p>
  </div>
  <div class="faq-q"><span class="ic">+</span>Welche Staaten können Evisitor für Australien in Anspruch nehmen?</div>
</section>

<aside class="faq-side">
  <p><a href="#">Visa-korvenet.org</a> ist ein nicht staatlicher Servicedienstleister für die Beantragung von Evisitor-Genehmigungen.</p>
  <p>Bei uns erhalten Sie die Evisitor-Einreisegenehmigung einschließlich unserer Serviceleistung. Jeder Antrag wird von einem deutschsprachigen Support Mitarbeiter geprüft und bearbeitet. Damit Sie ohne Probleme, z.B. Formfehler, nach Australien einreisen können.</p>
  <p>Sofern Sie den Antrag über uns anfordern, ist dieser 12 Monate ab Ausstellung gültig, es sein denn Ihr Reisepass läuft vorher ab.</p>
  <p>Sollten Sie die Evisitor Registrierungsnummer verlieren, so können Sie diese 12 Monate kostenfrei bei uns erneut in Ihrem Archiv abrufen. Neben dieser stehen Ihnen weitere Serviceleistungen zur Verfügung, diese Serviceleistung kostet 39 Euro und enthält alle anfallenden Gebühren.</p>
  <p>Sie können auch auf eigenes Risiko auf <a href="#">https://www.einreise-portal.example</a> Ihren Antrag stellen. Beachten Sie aber, dass Sie dann keine Unterstützung eines Live Supportmitarbeiters haben und die Gefahr besteht, fehlerhafte Eingaben zu tätigen.</p>
</aside>

<section class="callback ui">
  <div class="blue-side"></div>
  <h2 style="font-family:'Lato',sans-serif">Rückruf anfordern</h2>
  <p class="lead">Möchten Sie mit einem unserer Berater über das Telefon sprechen? Bitte reichen Sie Ihre Daten ein und wir werden uns in Kürze melden. Sie können uns auch mailen, wenn Sie es vorziehen würden.</p>
  <div class="label">Ich möchte gerne diskutieren:</div>
  <div class="field" style="left:666px;top:83px;width:208px">Touristen Visum
    <svg style="position:absolute;right:14px;top:15px" width="12" height="8"><polygon points="0,0 12,0 6,8" fill="#0b4f9e"/></svg></div>
  <div class="field" style="left:886px;top:83px;width:208px">Full Name</div>
  <div class="field" style="left:666px;top:131px;width:208px">Phone Number</div>
  <a class="send" href="#">RUF MICH AN</a>
</section>

<section class="map" role="img" aria-label="Straßenkarte mit Standort des Büros"></section>

<footer class="site-footer ui">
  <div class="foot-col" style="left:37px"><h3>Informationen</h3><a href="#">Gültigkeitsdauer ETA Visum</a></div>
  <div class="foot-col" style="left:299px"><h3>Quicklinks</h3><a href="#">ETA Formular deutsch</a><a href="#">Was ist ETA</a><a href="#">Touristen Visum</a><a href="#">Business Visum</a></div>
  <div class="foot-col" style="left:457px;top:48px"><a href="#">Was ist ETA</a><a href="#">AGB</a><a href="#">Kontakt</a></div>
  <div class="foot-col" style="left:625px"><h3>Weiteres</h3><a href="#">Datenschutz</a><a href="#">AGB</a><a href="#">Impressum</a></div>
  <div class="foot-help">
    <b>Sie brauchen Hilfe?</b><br>
    Service Hotline von Mo-Fr 10-16 Uhr<br>
    <b>Kostenfrei:</b> 0800 555210480
    <div class="cards"><span class="card-chip b"></span><span class="card-chip"></span><span class="card-chip c"></span></div>
  </div>
</footer>

</body>
</html>
```